Design a new jar label for a successful company

We are seeking a fresh label design that will be applied to a glass jar containing our high quality dried flower. We are a company based out of Washington State and we mainly sell dried herbs and oil extracts. The brand is "Copper Vale" and the product is "Copper Vale - Handcrafted Flower". I'd like to start with Black/Chrome as the color scheme, but we are open to other suggestions (for example dark purple instead of black). This will be professionally printed on a glossy label and the chrome or auxiliary colors can/will printed with a metallic foil.

BASIC REQUIREMENTS:

Size: 1.25" H x 2.5" L

Colors: Black and chrome. Preferably use a black background and make the logo/text chrome. Open to suggestions.

Margin: Please do not place any text within 1/16" around the edges to allow for deviation during die cutting process.

Logo: Use the Copper Vale shield as the center piece.

Required text: State "Handcrafted Flower" somewhere below the logo. Discretely place "TQDRN.COM" somewhere on the label.

Industry/Entity Type

Retail

Font styles to use
Other font styles liked:

Requirements
Must have
• The following warning most appear on the label. Please see attached graphic and also be sure to include the "21 and over" circular icon if possible:
• "Warning: This product has intoxicating effects and may be habit forming. Marijuana can impair concentration, coordination, and judgement. Do not operate a vehicle or machinery under the influence of this drug. There may be health risks associated with consumption of this product."
• "For use only by adults twenty-one and older. Keep out of reach of children."
• Note: You can use the circular 21 and over warning shown in the attached example instead of typing the text out.
Nice to have
• Fonts used - Doren Kessvik - FestivoLettersNo1.otf (This is the logo font.)
• Minion Pro - this is our standard copy font

```html
<!DOCTYPE html>
<html lang="en">
<head>
<meta charset="utf-8">
<title>Copper Vale - Handcrafted Flower Jar Labels</title>
<link rel="stylesheet" href="https://fonts.googleapis.com/css2?family=Crimson+Pro:wght@400;600&family=Oswald:wght@300;400;600&family=Playfair+Display+SC:wght@700&display=swap">
<style>
  :root {
    --page: #ffffff;
    --label-black: #0d0d0e;
    --label-black-edge: #1b1b1d;
    --label-plum: #2b0a20;
    --label-plum-edge: #3d1030;
    --chrome: #d9dade;
    --copy: #f2f2f2;
    --gold: #d9a955;
    --gold-deep: #8a6326;
    --pink: #d62a7f;
    --divider: rgba(255, 255, 255, 0.35);
  }
  * { box-sizing: border-box; margin: 0; padding: 0; }
  html, body {
    width: 1200px; height: 1188px; overflow: hidden;
    background: var(--page);
  }
  .sheet {
    position: relative; width: 1200px; height: 1188px;
    display: flex; flex-direction: column; align-items: center;
    gap: 36px; padding-top: 30px;
  }
  .label {
    position: relative; width: 1096px; height: 546px;
    display: grid; grid-template-columns: 304px 467px 325px;
    color: var(--copy);
  }
  .label--black { background: radial-gradient(ellipse at 50% 45%, var(--label-black-edge), var(--label-black) 70%); --accent: var(--gold); }
  .label--plum  { background: radial-gradient(ellipse at 50% 45%, var(--label-plum-edge), var(--label-plum) 70%); --accent: var(--pink); }

  .label__story {
    position: relative; padding: 64px 0 0 47px;
    border-right: 2px dotted var(--divider);
    margin: 34px 0; padding-top: 30px;
  }
  .strain-notes {
    font-family: "Crimson Pro", serif; font-size: 19px; line-height: 29px;
    text-transform: uppercase; letter-spacing: 0.2px; width: 245px;
  }
  .strain-notes em { font-style: normal; font-weight: 600; color: var(--gold); }
  .age-badge { position: absolute; left: 60px; top: 300px; width: 170px; height: 170px; }
  .age-badge text { font-family: Oswald, sans-serif; font-weight: 600; fill: var(--accent); }

  .label__brand {
    display: flex; flex-direction: column; align-items: center; padding-top: 70px;
  }
  .brand-name {
    font-family: Oswald, sans-serif; font-weight: 600; font-size: 68px;
    line-height: 74px; text-align: center; color: var(--chrome);
    letter-spacing: 2px; text-transform: uppercase;
  }
  .brand-ornament {
    width: 420px; height: 96px; margin-top: 40px; border-radius: 48px;
    background: radial-gradient(ellipse at center, var(--gold) 0%, var(--gold-deep) 55%, transparent 75%);
    opacity: 0.75;
  }
  .product-line {
    margin-top: 26px; font-family: "Playfair Display SC", serif; font-weight: 700;
    font-size: 30px; letter-spacing: 0.5px; color: var(--copy);
  }

  .label__warning {
    margin: 34px 0; padding: 30px 0 0 37px;
    border-left: 2px dotted var(--divider);
  }
  .warning-text {
    font-family: Oswald, sans-serif; font-weight: 300; font-size: 21.5px;
    line-height: 34.8px; width: 270px;
  }
  .site-url {
    margin-top: 26px; font-family: Oswald, sans-serif; font-weight: 400;
    font-size: 36px; color: var(--gold); letter-spacing: 0.5px;
  }
</style>
</head>
<body>
<main class="sheet">

  <section class="label label--black" aria-label="Copper Vale label, black edition">
    <div class="label__story">
      <p class="strain-notes">Green sticky and smelly just what you want from this strain. It is very powerful flower that will be sure to satisfy all those heavy indica smokers. <em>Enjoy!!</em></p>
      <svg class="age-badge" viewBox="0 0 170 170" aria-label="For use only by adults 21 or older">
        <defs><path id="ring-a" d="M85,85 m-66,0 a66,66 0 1,1 132,0 a66,66 0 1,1 -132,0"/></defs>
        <text font-size="20" letter-spacing="1"><textPath href="#ring-a" startOffset="2%">OLDER. FOR USE ONLY BY ADULTS 21 OR</textPath></text>
        <text x="85" y="106" font-size="62" text-anchor="middle">21</text>
      </svg>
    </div>
    <div class="label__brand">
      <h1 class="brand-name">Copper<br>Vale</h1>
      <div class="brand-ornament" role="img" aria-label="Gold foil flourish ornament"></div>
      <p class="product-line">Handcrafted Flower</p>
    </div>
    <div class="label__warning">
      <p class="warning-text">Warning: This product has intoxicating effects and may be habit forming. Marijuana can impair concentration, coordination, and judgement. Do not operate a vehicle or machinery under the influence of this drug. There may be health risks associated with consumption of this product.</p>
      <p class="site-url">TQDRN.COM</p>
    </div>
  </section>

  <section class="label label--plum" aria-label="Copper Vale label, plum edition">
    <div class="label__story">
      <p class="strain-notes">Green sticky and smelly just what you want from this strain. It is very powerful flower that will be sure to satisfy all those heavy indica smokers. <em>Enjoy!!</em></p>
      <svg class="age-badge" viewBox="0 0 170 170" aria-label="For use only by adults 21 or older">
        <defs><path id="ring-b" d="M85,85 m-66,0 a66,66 0 1,1 132,0 a66,66 0 1,1 -132,0"/></defs>
        <text font-size="20" letter-spacing="1"><textPath href="#ring-b" startOffset="2%">OLDER. FOR USE ONLY BY ADULTS 21 OR</textPath></text>
        <text x="85" y="106" font-size="62" text-anchor="middle">21</text>
      </svg>
    </div>
    <div class="label__brand">
      <h1 class="brand-name">Copper<br>Vale</h1>
      <div class="brand-ornament" role="img" aria-label="Gold foil flourish ornament"></div>
      <p class="product-line">Handcrafted Flower</p>
    </div>
    <div class="label__warning">
      <p class="warning-text">Warning: This product has intoxicating effects and may be habit forming. Marijuana can impair concentration, coordination, and judgement. Do not operate a vehicle or machinery under the influence of this drug. There may be health risks associated with consumption of this product.</p>
      <p class="site-url">TQDRN.COM</p>
    </div>
  </section>

</main>
</body>
</html>
```